BRV Stationary
BRV All The Way!
Corporate
Dale Orwick
CEO
2380 Tallow St. Suite #240 San Francisco, CA 94107
dorwick@brvatw.com
brvatw.com
looking for a water mark on the business cards and stationary. Check out the brief for the logo for more ideas. http://orders.markcraftdepot.com/contests/bright-relay-ventures/readbrief

```html
<!DOCTYPE html>
<html lang="en">
<head>
<meta charset="utf-8">
<title>BRV Stationary</title>
<link rel="stylesheet" href="https://fonts.googleapis.com/css2?family=Montserrat:wght@400;600;700&display=swap">
<style>
  :root {
    --backdrop: #e7e4df;
    --paper: #ffffff;
    --ink: #2b2b2b;
    --muted: #6d6d6d;
    --brand-blue: #3b5ba9;
    --brand-green: #5fb245;
    --card-dark: #1b1b1b;
    --shadow: 0 4px 14px rgba(0,0,0,0.18);
  }
  * { box-sizing: border-box; margin: 0; padding: 0; }
  html, body { width: 1200px; height: 737px; overflow: hidden; }
  body {
    background: var(--backdrop);
    font-family: "Montserrat", sans-serif;
    color: var(--ink);
    position: relative;
  }
  .sheet {
    position: absolute;
    background: var(--paper);
    box-shadow: var(--shadow);
    overflow: hidden;
  }
  .brand-name {
    font-weight: 700;
    color: var(--brand-blue);
    letter-spacing: 0.02em;
    line-height: 1;
  }
  .small-print { font-size: 7px; line-height: 1.5; color: var(--muted); }
  .corner-accent { position: absolute; right: 0; bottom: 0; }

  /* Letterhead */
  .letterhead { left: 250px; top: 70px; width: 420px; height: 594px; }
  .letterhead .brand-name { position: absolute; left: 34px; top: 34px; font-size: 44px; }
  .letterhead .footer-address { position: absolute; left: 34px; bottom: 26px; }

  /* Envelope back */
  .envelope-back { left: 710px; top: 40px; width: 420px; height: 190px; }
  .envelope-back .flap { position: absolute; left: 0; top: 0; }
  .envelope-back .brand-name { position: absolute; right: 40px; top: 112px; font-size: 26px; }

  /* Envelope front */
  .envelope-front { left: 710px; top: 258px; width: 420px; height: 190px; }
  .envelope-front .brand-name { position: absolute; left: 22px; top: 20px; font-size: 36px; }
  .envelope-front .return-address { position: absolute; left: 22px; top: 66px; }

  /* Business cards */
  .card { width: 200px; height: 114px; }
  .card .brand-name { font-size: 26px; }
  .card-dark { background: var(--card-dark); }
  .card-dark .small-print { color: #bdbdbd; }
  .card-dark .person-name { color: #ffffff; }

  .card-front-dark { left: 30px; top: 250px; }
  .card-back-dark  { left: 30px; top: 390px; }
  .card-front-light { left: 710px; top: 480px; }
  .card-back-light  { left: 930px; top: 480px; }

  .card-front .brand-name { position: absolute; right: 14px; top: 12px; font-size: 22px; }
  .card-front .contact { position: absolute; left: 14px; top: 46px; }
  .person-name { font-size: 9px; font-weight: 700; color: var(--ink); }
  .person-title { font-size: 7px; font-weight: 600; color: var(--brand-green); margin-bottom: 4px; }

  .card-back { display: flex; flex-direction: column; align-items: center; justify-content: center; gap: 12px; }
  .card-back .web { font-size: 7px; color: var(--muted); letter-spacing: 0.08em; }
  .card-dark .web { color: #bdbdbd; }
</style>
</head>
<body>

  <!-- Letterhead -->
  <section class="sheet letterhead">
    <div class="brand-name">BRV</div>
    <p class="small-print footer-address">
      2380 Tallow St. Suite #240 San Francisco, CA 94107<br>
      p: 415.555.0148 &nbsp; f: 415.555.0149 &nbsp; e: dorwick@brvatw.com
    </p>
    <svg class="corner-accent" width="70" height="70" viewBox="0 0 70 70">
      <polygon points="70,0 70,70 0,70" fill="var(--brand-green)"/>
      <polygon points="70,30 70,70 30,70" fill="var(--brand-blue)"/>
    </svg>
  </section>

  <!-- Envelope back -->
  <section class="sheet envelope-back">
    <svg class="flap" width="420" height="190" viewBox="0 0 420 190">
      <polygon points="0,0 420,0 250,100 170,100" fill="var(--card-dark)"/>
      <polyline points="0,190 190,95 230,95 420,190" fill="none" stroke="#dcdcdc" stroke-width="1"/>
    </svg>
    <div class="brand-name">BRV</div>
  </section>

  <!-- Envelope front -->
  <section class="sheet envelope-front">
    <div class="brand-name">BRV</div>
    <p class="small-print return-address">2380 Tallow St. Suite #240 San Francisco, CA 94107</p>
    <svg class="corner-accent" width="44" height="44" viewBox="0 0 44 44">
      <polygon points="44,0 44,44 0,44" fill="var(--brand-green)"/>
      <polygon points="44,20 44,44 20,44" fill="var(--brand-blue)"/>
    </svg>
  </section>

  <!-- Dark business card front -->
  <section class="sheet card card-dark card-front card-front-dark">
    <div class="brand-name">BRV</div>
    <div class="contact">
      <p class="person-name">Dale Orwick</p>
      <p class="person-title">CEO</p>
      <p class="small-print">2380 Tallow St. Suite #240<br>San Francisco, CA 94107<br>p: 415.555.0148<br>dorwick@brvatw.com</p>
    </div>
    <svg class="corner-accent" width="34" height="34" viewBox="0 0 34 34">
      <polygon points="34,0 34,34 0,34" fill="var(--brand-green)"/>
      <polygon points="34,16 34,34 16,34" fill="var(--brand-blue)"/>
    </svg>
  </section>

  <!-- Dark business card back -->
  <section class="sheet card card-dark card-back card-back-dark">
    <div class="brand-name">BRV</div>
    <p class="web">www.brvatw.com</p>
  </section>

  <!-- Light business card front -->
  <section class="sheet card card-front card-front-light">
    <div class="brand-name">BRV</div>
    <div class="contact">
      <p class="person-name">Dale Orwick</p>
      <p class="person-title">CEO</p>
      <p class="small-print">2380 Tallow St. Suite #240<br>San Francisco, CA 94107<br>p: 415.555.0148<br>dorwick@brvatw.com</p>
    </div>
    <svg class="corner-accent" width="34" height="34" viewBox="0 0 34 34">
      <polygon points="34,0 34,34 0,34" fill="var(--brand-green)"/>
      <polygon points="34,16 34,34 16,34" fill="var(--brand-blue)"/>
    </svg>
  </section>

  <!-- Light business card back -->
  <section class="sheet card card-back card-back-light">
    <div class="brand-name">BRV</div>
    <p class="web">www.brvatw.com</p>
  </section>

</body>
</html>
```